Business card design for crowd sourced review site.

I need a business card magnet design for an online, crowd-sourced, restaurant review site strictly for Kosher restaurants.
It is similar to RoamLedger but catering to a very particular crowd.
The markets it will be distributed in are flooded with business card fridge magnets so this needs to be eye-catching and unique. The Business name is PlateMarks
The website isnt finished but you can see the basic setup here
http://restaurant.vintrello.com/

The second image i included is another logo design I liked and was thinking about using and decided I will probably also make a SECOND custom cut business card in the shape of that icon. Bonus if you can throw that in also.

Target Market(s)

Jewish consumers aged 20-35

Industry/Entity Type

Business

Contact Information for Business Card

see description.
Design should not be too crowded and should in eye-catching. Will mainly be used as fridge magnets.

Requirements
Must have
• Website address. logo.
Nice to have
• tagline. (The Definitive guide to kosher dining for the Kosher consumer)
• Im not a professional but I personally think the color blue goes along with this concept. ill leave it to you to decide.
Should not have
• any religious symbols.

```html
<!DOCTYPE html>
<html lang="en">
<head>
<meta charset="utf-8">
<title>PlateMarks Business Card</title>
<link rel="stylesheet" href="https://fonts.googleapis.com/css2?family=Roboto:wght@300;400;700&display=swap">
<style>
  :root {
    --stage: #3a3a3a;
    --brand-red: #e03a24;
    --card-black: #0b0b0b;
    --ink-white: #ffffff;
    --ink-soft: #e6e6e6;
  }
  * { box-sizing: border-box; margin: 0; padding: 0; }
  html, body {
    width: 1200px; height: 950px; overflow: hidden;
    background: var(--stage);
    font-family: "Roboto", Arial, sans-serif;
  }
  .sheet {
    width: 1200px; height: 950px;
    display: flex; flex-direction: column; align-items: center; justify-content: center;
    gap: 36px;
  }
  .card {
    position: relative;
    width: 740px; height: 423px;
    overflow: hidden;
    box-shadow: 0 10px 30px rgba(0,0,0,.45);
  }
  .card--front { background: var(--brand-red); color: var(--ink-white); }
  .card--back { background: var(--card-black); color: var(--ink-white); }

  .brand {
    display: flex; align-items: center; gap: 14px;
    font-weight: 700; letter-spacing: .5px;
  }
  .brand__dot { border-radius: 50%; flex: none; }

  .card--front .brand {
    position: absolute; left: 0; right: 0; top: 140px;
    justify-content: center; font-size: 62px; color: var(--ink-white);
  }
  .card--front .brand__dot { width: 30px; height: 30px; background: var(--ink-white); }
  .tagline {
    position: absolute; left: 0; right: 0; top: 268px;
    text-align: center; font-size: 15px; font-weight: 400; color: var(--ink-white);
  }

  .card--back .brand {
    position: absolute; left: 150px; top: 92px;
    font-size: 52px; color: var(--ink-white);
  }
  .card--back .brand__dot { width: 26px; height: 26px; background: var(--brand-red); }

  .rule {
    position: absolute; left: 330px; right: 36px; top: 196px;
    height: 1px; background: var(--brand-red);
  }

  .contact {
    position: absolute; right: 40px; top: 212px;
    list-style: none; text-align: right; font-size: 15px; line-height: 24px; color: var(--ink-soft);
  }
  .contact li { display: flex; align-items: center; justify-content: flex-end; gap: 10px; }
  .contact svg { width: 14px; height: 14px; fill: var(--brand-red); }
  .contact .contact__email { padding-right: 24px; }

  .person {
    position: absolute; left: 48px; top: 300px;
  }
  .person__bar { width: 100px; height: 3px; background: var(--ink-white); margin-bottom: 10px; }
  .person__name { font-size: 20px; font-weight: 400; color: var(--brand-red); }
  .person__role { font-size: 16px; color: var(--ink-white); margin-bottom: 10px; }
  .person__address { font-style: normal; font-size: 15px; line-height: 21px; color: var(--ink-soft); }

  .web-band {
    position: absolute; left: 300px; right: 0; bottom: 0; height: 62px;
    background: var(--brand-red);
    display: flex; align-items: center; justify-content: center;
    font-size: 17px; font-weight: 700; letter-spacing: 6px; color: var(--ink-white);
  }
</style>
</head>
<body>
<main class="sheet">
  <section class="card card--front" aria-label="Card front">
    <div class="brand"><span class="brand__dot"></span><span class="brand__name">PlateMarks</span></div>
    <p class="tagline">The Definitive guide to kosher dining for the Kosher consumer</p>
  </section>

  <section class="card card--back" aria-label="Card back">
    <div class="brand"><span class="brand__dot"></span><span class="brand__name">PlateMarks</span></div>
    <div class="rule"></div>

    <ul class="contact">
      <li>555 0147 2231
        <svg viewBox="0 0 24 24" aria-hidden="true"><path d="M6.6 10.8a15 15 0 0 0 6.6 6.6l2.2-2.2c.3-.3.7-.4 1-.2 1.1.4 2.3.6 3.6.6.6 0 1 .4 1 1V20c0 .6-.4 1-1 1A17 17 0 0 1 3 4c0-.6.4-1 1-1h3.5c.6 0 1 .4 1 1 0 1.3.2 2.5.6 3.6.1.3 0 .7-.2 1z"/></svg>
      </li>
      <li>555 0193 4418
        <svg viewBox="0 0 24 24" aria-hidden="true"><path d="M7 1h10a2 2 0 0 1 2 2v18a2 2 0 0 1-2 2H7a2 2 0 0 1-2-2V3a2 2 0 0 1 2-2zm0 3v14h10V4zm5 15.5a1 1 0 1 0 0 2 1 1 0 0 0 0-2z"/></svg>
      </li>
      <li>555 0162 7704
        <svg viewBox="0 0 24 24" aria-hidden="true"><path d="M6 2h10v5H6zM4 8h16a2 2 0 0 1 2 2v7h-4v5H6v-5H2v-7a2 2 0 0 1 2-2zm4 7v5h8v-5z"/></svg>
      </li>
      <li>ari@platemarks.com
        <svg viewBox="0 0 24 24" aria-hidden="true"><path d="M2 5h20v14H2zm2 2v.5l8 5 8-5V7l-8 5z"/></svg>
      </li>
    </ul>

    <div class="person">
      <div class="person__bar"></div>
      <h2 class="person__name">Ari Weller</h2>
      <p class="person__role">President</p>
      <address class="person__address">4127 Linden Row Drive<br>Oak Hollow, NY 11920</address>
    </div>

    <div class="web-band">www.platemarks.com</div>
  </section>
</main>
</body>
</html>
```